Company Capability Brochure

Want to create a mulit paged brochure to hand out to potential clients to show our services and capabilities.

Attached is a rough draft we made using chatgpt which can be use as an example and includes the categories, text, our logo and preferred colour scheme we wish to use.
Would like to make this more look more visually appealing and a more professional layout over more pages.

```html
<!DOCTYPE html>
<html lang="en">
<head>
<meta charset="utf-8">
<title>Vigilant Security Services – Capability Brochure</title>
<link rel="stylesheet" href="https://fonts.googleapis.com/css2?family=Archivo+Black&family=Arimo:wght@400;700&display=swap">
<style>
  :root {
    --backdrop: #d6d6d8;
    --paper: #f7f7f8;
    --navy: #13284f;
    --navy-deep: #0b1a38;
    --blue: #1f5b93;
    --sky: #2b86c5;
    --ink: #1b1b1f;
    --muted: #3a3a40;
    --head: "Archivo Black", "Arial Black", sans-serif;
    --body: "Arimo", Arial, sans-serif;
  }
  * { box-sizing: border-box; margin: 0; padding: 0; }
  html, body { width: 828px; height: 1200px; overflow: hidden; }
  body { background: var(--backdrop); font-family: var(--body); color: var(--ink); position: relative; }

  .spread { position: absolute; left: 24px; width: 780px; height: 551px; box-shadow: 0 6px 18px rgba(0,0,0,.18); }
  .spread--covers { top: 30px; }
  .spread--inside { top: 619px; }
  .page { position: absolute; top: 0; width: 390px; height: 551px; background: var(--paper); overflow: hidden; }
  .page--left { left: 0; }
  .page--right { left: 390px; }
  .page__art { position: absolute; inset: 0; width: 390px; height: 551px; }
  .spine { position: absolute; left: 382px; top: 0; width: 16px; height: 551px;
    background: linear-gradient(90deg, rgba(0,0,0,0) 0%, rgba(0,0,0,.08) 50%, rgba(0,0,0,0) 100%); pointer-events: none; }

  /* Back cover */
  .clients { position: absolute; left: 30px; top: 170px; }
  .section-title { font-family: var(--body); font-weight: 700; font-size: 13px; color: var(--ink); letter-spacing: .2px; }
  .clients__list { list-style: none; margin-top: 8px; font-size: 8.5px; line-height: 12.5px; }
  .clients__list li::before { content: ""; display: inline-block; width: 3.5px; height: 3.5px; background: var(--ink); margin: 0 5px 1px 0; }
  .contact { position: absolute; right: 118px; top: 378px; list-style: none; font-size: 8px; line-height: 15px; text-align: right; }
  .contact li { display: flex; align-items: center; justify-content: flex-end; gap: 6px; }
  .contact svg { width: 9px; height: 9px; fill: var(--ink); flex: none; }
  .licence { position: absolute; left: 246px; top: 478px; font-size: 11.5px; line-height: 14px; }
  .licence strong { display: block; font-weight: 700; }

  /* Front cover */
  .brand { position: absolute; left: 150px; top: 30px; display: flex; align-items: center; gap: 7px;
    font-family: var(--body); font-weight: 700; font-size: 12px; color: var(--blue); letter-spacing: .4px; }
  .brand__dot { width: 14px; height: 14px; border-radius: 50%; background: var(--blue); }
  .tagline { position: absolute; left: 52px; top: 196px; width: 270px; text-align: center;
    font-family: var(--head); font-size: 23px; line-height: 27px; color: #fff; }

  /* Inside left */
  .statement { position: absolute; }
  .statement h2 { font-family: var(--body); font-weight: 700; font-size: 11.5px; line-height: 12px; color: var(--navy); text-transform: uppercase; margin-bottom: 7px; }
  .statement p { font-size: 6.4px; line-height: 8.3px; text-align: justify; color: var(--muted); }
  .statement--vision { left: 210px; top: 196px; width: 160px; }
  .statement--mission { left: 30px; top: 262px; width: 168px; }
  .statement--culture { left: 30px; top: 448px; width: 335px; }

  /* Inside right */
  .services-title { position: absolute; left: 196px; top: 34px; font-family: var(--body); font-weight: 700; font-size: 12px; color: var(--navy); }
  .service { position: absolute; left: 0; width: 390px; height: 84px; }
  .service__art { position: absolute; left: 0; top: 0; width: 190px; height: 84px; }
  .service__label { position: absolute; left: 40px; top: 26px; width: 90px; font-weight: 700; font-size: 11px; line-height: 12px; color: #fff; text-transform: uppercase; letter-spacing: .3px; }
  .service__text { position: absolute; left: 198px; top: 4px; width: 172px; font-size: 6.4px; line-height: 8.4px; text-align: justify; color: var(--muted); }
</style>
</head>
<body>

<!-- Spread 1: back cover + front cover -->
<section class="spread spread--covers">
  <article class="page page--left back-cover">
    <svg class="page__art" viewBox="0 0 390 551" aria-hidden="false">
      <defs>
        <linearGradient id="cityNight" x1="0" y1="0" x2="1" y2="1">
          <stop offset="0" stop-color="#6b3f8f"/>
          <stop offset=".35" stop-color="#2c4f9a"/>
          <stop offset=".6" stop-color="#b4552e"/>
          <stop offset="1" stop-color="#172a5c"/>
        </linearGradient>
      </defs>
      <path role="img" aria-label="Night-time city skyline with light trails and network lines" fill="url(#cityNight)"
            d="M140,0 H390 V470 C305,430 235,340 198,235 C170,155 148,80 140,0 Z"/>
    </svg>

    <div class="clients">
      <h2 class="section-title">OUR CLIENTS</h2>
      <ul class="clients__list">
        <li>Harbourline Hotel Parkside</li>
        <li>Crestview Hotel Parkside</li>
        <li>Westbrook College</li>
        <li>Summit Body Corporate</li>
        <li>Hale &amp; Morrow</li>
        <li>Strata Select</li>
        <li>QRTM</li>
        <li>Bellwood Strata</li>
        <li>Riverton Rugby League Club</li>
        <li>Ashford</li>
      </ul>
    </div>

    <ul class="contact">
      <li>1300 555 019 <svg viewBox="0 0 10 10"><path d="M2 0.5 3.8 2.8 2.9 4a6 6 0 0 0 3.1 3.1l1.2-.9 2.3 1.8-1 1.5C4.8 9.5.5 5.2.5 1.5Z"/></svg></li>
      <li>info@vigilantsecurity.example <svg viewBox="0 0 10 10"><path d="M0 2h10v6H0Z M0.8 2.6 5 5.6 9.2 2.6" fill="none" stroke="#1b1b1f" stroke-width="1"/></svg></li>
      <li>www.vigilantsecurityservices.example <svg viewBox="0 0 10 10"><circle cx="5" cy="5" r="4.3" fill="none" stroke="#1b1b1f" stroke-width="1"/><path d="M0.7 5h8.6M5 .7v8.6" stroke="#1b1b1f" stroke-width=".8"/><ellipse cx="5" cy="5" rx="2" ry="4.3" fill="none" stroke="#1b1b1f" stroke-width=".8"/></svg></li>
      <li>12/8 Harlow Rd, Eastmere, NSW 2100 <svg viewBox="0 0 10 10"><path d="M5 0a3.5 3.5 0 0 1 3.5 3.5C8.5 6 5 10 5 10S1.5 6 1.5 3.5A3.5 3.5 0 0 1 5 0Zm0 2a1.5 1.5 0 1 0 0 3 1.5 1.5 0 0 0 0-3Z"/></svg></li>
    </ul>

    <p class="licence"><strong>Master License:</strong>40012345</p>
  </article>

  <article class="page page--right front-cover">
    <svg class="page__art" viewBox="0 0 390 551">
      <defs>
        <linearGradient id="cityMono" x1="0" y1="0" x2="1" y2="1">
          <stop offset="0" stop-color="#f2f2f3"/>
          <stop offset="1" stop-color="#a9abb0"/>
        </linearGradient>
        <linearGradient id="cityDusk" x1="0" y1="0" x2="1" y2="1">
          <stop offset="0" stop-color="#2b3f7a"/>
          <stop offset=".5" stop-color="#1a2a58"/>
          <stop offset="1" stop-color="#4a3a6a"/>
        </linearGradient>
        <linearGradient id="shieldFill" x1="0" y1="0" x2="0" y2="1">
          <stop offset="0" stop-color="#2a6aa6"/>
          <stop offset="1" stop-color="#123a6b"/>
        </linearGradient>
      </defs>
      <path role="img" aria-label="Grey city aerial view with a security camera mounted at the right"
            fill="url(#cityMono)" d="M20,62 L390,40 V360 L300,372 C230,300 120,250 20,250 Z"/>
      <path role="img" aria-label="Dusk city street with glowing network lines"
            fill="url(#cityDusk)" d="M150,551 C210,470 290,410 390,378 V551 Z"/>
      <path fill="url(#shieldFill)" stroke="#fff" stroke-width="5"
            d="M34,170 C110,172 190,150 246,104 C280,140 320,160 356,168 L348,238 C336,350 270,430 178,482 C96,440 42,350 34,250 Z"/>
    </svg>
    <div class="brand"><span class="brand__dot"></span>VIGILANT SECURITY SERVICES</div>
    <h1 class="tagline">Be Informed and Make The Right Choice</h1>
  </article>
  <div class="spine"></div>
</section>

<!-- Spread 2: inside pages -->
<section class="spread spread--inside">
  <article class="page page--left about">
    <svg class="page__art" viewBox="0 0 390 551">
      <defs>
        <linearGradient id="smartHome" x1="0" y1="0" x2="1" y2="0">
          <stop offset="0" stop-color="#c9d4e2"/>
          <stop offset=".45" stop-color="#3a4f74"/>
          <stop offset=".6" stop-color="#e6e6e8"/>
          <stop offset="1" stop-color="#b9b6b2"/>
        </linearGradient>
      </defs>
      <path role="img" aria-label="Home security camera beside a hand holding a phone showing live camera feeds, dome camera above"
            fill="url(#smartHome)" d="M0,0 H390 V128 C340,134 300,150 262,172 L0,232 Z"/>
      <path fill="var(--navy)" d="M0,232 L262,172 C300,150 340,134 390,128 V138 C342,144 304,160 266,182 L0,242 Z"/>
    </svg>

    <div class="statement statement--vision">
      <h2>Vision<br>Statement</h2>
      <p>Our vision is to be the most trusted, innovative, and customer focused partner in the security industry, renowned for the professional installation, service, and maintenance of Electronic and Mechanical Security Systems. We strive to set the benchmark for excellence by delivering tailored, reliable, and future-ready solutions that protect what matters most to our clients, while building lasting relationships based on integrity, responsiveness, and continuous improvement.</p>
    </div>

    <div class="statement statement--mission">
      <h2>Mission<br>Statement</h2>
      <p>Our mission is to deliver exceptional service and cutting-edge Electronic and Mechanical Security Solutions that not only meet but consistently exceed our clients' expectations. We are dedicated to ensuring the safety, protection, and peace of mind of those we serve by combining advanced technologies, industry expertise, and a relentless focus on quality, reliability, and customer satisfaction. Through personalized solutions, responsive support, and continuous innovation, we aim to build long-term partnerships and be a trusted name in security.</p>
    </div>

    <div class="statement statement--culture">
      <h2>Culture Statement</h2>
      <p>At the heart of our company is a culture driven by trust, innovation, and service excellence. We are a team of dedicated professionals who take pride in protecting what matters most to our clients through advanced Electronic and Mechanical Security Solutions. We cultivate a work environment built on integrity, mutual respect, and accountability, where every team member is empowered to grow, contribute ideas, and take ownership of outcomes. Collaboration, continuous improvement, and a commitment to exceeding expectations define how we operate, both with our clients and each other. We embrace change, champion innovation, and remain agile in an evolving industry, always striving to deliver smarter, more reliable, and more secure solutions. Together, we are building not just systems, but lasting partnerships and a safer future.</p>
    </div>
  </article>

  <article class="page page--right services">
    <h2 class="services-title">OUR SERVICES</h2>

    <div class="service" style="top:62px">
      <svg class="service__art" viewBox="0 0 190 84">
        <path fill="var(--navy)" d="M0,22 L150,10 V70 L0,78 Z"/>
        <path role="img" aria-label="Bullet CCTV camera against a city skyline" fill="#7f9dbd" stroke="#fff" stroke-width="3" d="M118,14 C138,14 156,8 168,2 C174,8 182,12 188,14 L186,40 C182,62 168,76 152,84 C132,74 120,56 118,38 Z"/>
      </svg>
      <span class="service__label">CCTV<br>Systems</span>
      <p class="service__text">Protect your home or office from theft and vandalism with security systems that monitor for intruders day and night using infrared capability. Each system is customised to your property's needs and offers remote camera viewing for added peace of mind.</p>
    </div>

    <div class="service" style="top:154px">
      <svg class="service__art" viewBox="0 0 190 84">
        <path fill="var(--navy)" d="M0,22 L150,10 V70 L0,78 Z"/>
        <path role="img" aria-label="Hand using a keypad access control reader" fill="#6f8799" stroke="#fff" stroke-width="3" d="M118,14 C138,14 156,8 168,2 C174,8 182,12 188,14 L186,40 C182,62 168,76 152,84 C132,74 120,56 118,38 Z"/>
      </svg>
      <span class="service__label">Access<br>Control</span>
      <p class="service__text">Access control systems boost security by granting entry only to authorised users and tracking staff movements and hours. Strata can manage access levels for specific floors or rooms, prevent risks from copied keys, and quickly disable or replace lost key-fobs.</p>
    </div>

    <div class="service" style="top:246px">
      <svg class="service__art" viewBox="0 0 190 84">
        <path fill="var(--navy)" d="M0,22 L150,10 V70 L0,78 Z"/>
        <path role="img" aria-label="Wall-mounted intercom panel beside a wooden door" fill="#8a6a4c" stroke="#fff" stroke-width="3" d="M118,14 C138,14 156,8 168,2 C174,8 182,12 188,14 L186,40 C182,62 168,76 152,84 C132,74 120,56 118,38 Z"/>
      </svg>
      <span class="service__label">Inter-<br>Coms</span>
      <p class="service__text">Intercom systems, common in offices and apartments, enable easy communication from entry doors to internal handsets. Our skilled technicians install, service, and upgrade a wide range of systems to suit all residents' needs.</p>
    </div>

    <div class="service" style="top:338px">
      <svg class="service__art" viewBox="0 0 190 84">
        <path fill="var(--navy)" d="M0,22 L150,10 V70 L0,78 Z"/>
        <path role="img" aria-label="Hand setting a wall alarm keypad" fill="#cfcac6" stroke="#fff" stroke-width="3" d="M118,14 C138,14 156,8 168,2 C174,8 182,12 188,14 L186,40 C182,62 168,76 152,84 C132,74 120,56 118,38 Z"/>
      </svg>
      <span class="service__label">Alarms</span>
      <p class="service__text">Alarm systems protect premises from intruders and give residents peace of mind when away. With integrated alarm monitoring, your property stays secure even when unoccupied, tailored to meet needs from simple to advanced setups.</p>
    </div>

    <div class="service" style="top:430px">
      <svg class="service__art" viewBox="0 0 190 84">
        <path fill="var(--navy)" d="M0,22 L150,10 V70 L0,78 Z"/>
        <path role="img" aria-label="Gate entry camera and keypad panel" fill="#9aa3ab" stroke="#fff" stroke-width="3" d="M118,14 C138,14 156,8 168,2 C174,8 182,12 188,14 L186,40 C182,62 168,76 152,84 C132,74 120,56 118,38 Z"/>
      </svg>
      <span class="service__label">Gates</span>
      <p class="service__text">Gate camera security safeguards your property by monitoring entry points and recording all activity. With high-resolution day and night vision, it ensures clear footage in any light. Systems can be tailored to your needs and offer remote viewing for real-time access from anywhere.</p>
    </div>
  </article>
  <div class="spine"></div>
</section>

</body>
</html>
```